Newsletter Kellos-Track-Weeks

Hello i need some Newsletter to promote my company and the new events that we make.
we are organist motorbike events in different circuits in europe

please wrote me when you need some other format from the logo

I need a Template that include the text blocks. in the moment i don’t have finish the text.

we need the newsletter to send in sozialmedia, e-mail and homepage.
its always for online we don’t print and send newsletter.

i will send the newsletters with the program swift post

Target Market(s)

us target market are all motorbike stores and all motorbike riders.

Industry/Entity Type

Events

Requirements
Must have
• i don’t know :)
have to be us logo and see very cool and crazy..
My Homepage maybe can help
www.kellos-track-weeks.ch
Nice to have
• a link to my contact e-mail and web address

```html
<!DOCTYPE html>
<html lang="en">
<head>
<meta charset="UTF-8">
<title>Track Event Newsletter</title>
<link rel="stylesheet" href="https://fonts.googleapis.com/css2?family=Oswald:wght@700&family=Roboto+Condensed:wght@400&display=swap">
<style>
  :root {
    --page: #ffffff;
    --panel: #000000;
    --footer-top: #1a1a1a;
    --footer-bottom: #0c0c0c;
    --red: #e0101c;
    --contact-red: #c8101a;
    --grey-heading: #9a9a9a;
    --text: #ffffff;
    --photo-sky: #a9aba4;
    --photo-track: #5c5e60;
    --photo-bike: #b32a2a;
    --lot: #8d8f91;
  }
  * { margin: 0; padding: 0; box-sizing: border-box; }
  html, body { width: 777px; height: 1200px; overflow: hidden; background: var(--page); }
  .newsletter {
    position: absolute; left: 63px; top: 64px;
    width: 648px; height: 1077px;
    background: var(--panel);
    font-family: "Roboto Condensed", "Arial Narrow", sans-serif;
    color: var(--text);
    overflow: hidden;
  }
  .hero { position: absolute; left: 0; top: 0; width: 648px; height: 330px; display: block; }
  .subheading, .heading {
    position: absolute; right: 33px;
    font-family: "Oswald", "Arial Narrow", sans-serif; font-weight: 700;
    text-transform: uppercase; line-height: 1; white-space: nowrap;
  }
  .subheading { top: 306px; font-size: 24px; letter-spacing: 1.2px; color: var(--grey-heading); }
  .heading { top: 334px; font-size: 45px; letter-spacing: 2.6px; color: var(--red); }
  .intro {
    position: absolute; left: 27px; right: 33px; top: 406px;
    font-size: 17px; line-height: 27px; text-align: justify;
  }
  .story { position: absolute; left: 27px; width: 315px; }
  .story-title { font-size: 17px; line-height: 27px; color: var(--red); font-weight: 400; }
  .story-body { font-size: 15.5px; line-height: 27px; }
  .story--first { top: 510px; }
  .story--second { top: 708px; }
  .story-photo {
    position: absolute; display: block;
    background: linear-gradient(135deg, var(--lot) 0%, #c9c9c9 45%, var(--photo-bike) 70%, #6f7072 100%);
  }
  .story-photo--first { left: 368px; top: 517px; width: 253px; height: 136px; border: 3px solid var(--red); }
  .story-photo--second { left: 364px; top: 720px; width: 251px; height: 135px; border: 3px solid var(--text); }
  .footer {
    position: absolute; left: 0; top: 927px; width: 648px; height: 150px;
    background: linear-gradient(180deg, var(--footer-top), var(--footer-bottom));
  }
  .footer-title { position: absolute; left: 39px; top: 16px; font-size: 22px; }
  .contact-line { position: absolute; font-size: 20px; line-height: 24px; white-space: nowrap; }
  .contact-line--phone { left: 39px; top: 58px; color: var(--contact-red); }
  .contact-line--email { left: 39px; top: 96px; color: var(--contact-red); }
  .contact-line--address1 { left: 425px; top: 58px; }
  .contact-line--address2 { left: 425px; top: 96px; }
</style>
</head>
<body>
  <main class="newsletter">
    <svg class="hero" viewBox="0 0 648 330" role="img" aria-label="Photo of two riders leaning their red sport motorbikes into a track corner">
      <defs>
        <linearGradient id="hero-tone" x1="0" y1="0" x2="0" y2="1">
          <stop offset="0" stop-color="#a9aba4"/>
          <stop offset="0.35" stop-color="#8e9188"/>
          <stop offset="0.55" stop-color="#5c5e60"/>
          <stop offset="1" stop-color="#4a4c4e"/>
        </linearGradient>
        <radialGradient id="hero-bikes" cx="0.4" cy="0.6" r="0.45">
          <stop offset="0" stop-color="#b32a2a" stop-opacity="0.55"/>
          <stop offset="1" stop-color="#b32a2a" stop-opacity="0"/>
        </radialGradient>
      </defs>
      <polygon points="0,0 648,0 648,243 0,329" fill="url(#hero-tone)"/>
      <polygon points="0,0 648,0 648,243 0,329" fill="url(#hero-bikes)"/>
    </svg>

    <p class="subheading">Sub heading here</p>
    <h1 class="heading">Heading here</h1>

    <p class="intro">Lorem ipsum dolor sit ipsum Lorem&nbsp; Lorem ipsum dolor sit ipsum Lorem Lorem ipsum dolor sit ipsum Lorem Lorem ipsum dolor sit ipsum Lorem&nbsp; Lorem ipsum dolor sit ipsum Lorem Lorem ipsum dolor sit ipsum Lorem</p>

    <section class="story story--first">
      <h2 class="story-title">Lorem ipsum dolor sit ipsum Lorem</h2>
      <p class="story-body">Lorem ipsum dolor sit ipsum Lorem&nbsp; Lorem ipsum dolor sit ipsum Lorem Lorem ipsum dolor sit ipsum Lorem Lorem ipsum dolor sit ipsum Lorem&nbsp; Lorem ipsum dolor sit ipsum Lorem Lorem ipsum dolor sit ipsum Lorem</p>
    </section>
    <div class="story-photo story-photo--first" role="img" aria-label="Aerial photo of the paddock with parked motorbikes and team tents"></div>

    <section class="story story--second">
      <h2 class="story-title">Lorem ipsum dolor sit ipsum Lorem</h2>
      <p class="story-body">Lorem ipsum dolor sit ipsum Lorem&nbsp; Lorem ipsum dolor sit ipsum Lorem Lorem ipsum dolor sit ipsum Lorem Lorem ipsum dolor sit ipsum Lorem&nbsp; Lorem ipsum dolor sit ipsum Lorem Lorem ipsum dolor sit ipsum Lorem</p>
    </section>
    <div class="story-photo story-photo--second" role="img" aria-label="Aerial photo of riders gathered in the paddock beside the pit building"></div>

    <footer class="footer">
      <p class="footer-title">Contact details here</p>
      <p class="contact-line contact-line--phone">Phone&nbsp; : 0 123&nbsp; 4654646</p>
      <p class="contact-line contact-line--email">Email&nbsp;&nbsp; : info@email.com</p>
      <p class="contact-line contact-line--address1">Address Line Here 1</p>
      <p class="contact-line contact-line--address2">Address Line Here 2</p>
    </footer>
  </main>
</body>
</html>
```